Lab & Medical Equipment Repair Company Business Card Design

Looking for business card design for a lab & medical equipment repair company. Must be double-sided and must list our primary pieces we repair. Optionally, can include a QR code which should direct to our website.

Clients are usually doctors, so the card must be designed with a professional tone; however, we are looking for creativity in presentation. Open as to what should be on the front and back on card.

** Looking for a CLEAN design with creativity. Please use "Nice to have Priorities" items with discretion.

Core marketing logic:

When lab or medical equipment needs repair, most doctors call the manufacturers and schedule a technician to repair. Usually this takes one or two weeks, and, often, their work spoils. Alternatively, the doctors could hold equipment insurance which gives them a less expensive cost, but the response time is still similarly long.

Our company provides both competitive rates and one of the fastest response times in the industry. Technicians are dispatched directly to the site of the equipment, usually within 24 hours. Equipment under contract receives the same fast response time and includes complimentary annual maintenance. We service some of the most prestigious facilities in the Pittsburgh area and cover all of Western Pennsylvania, Ohio, and West Virginia.

Target Market(s)

Laboratory owners (doctors)

Industry/Entity Type

Marketing

Requirements
Must have
• Company Logo
Employee Name: Ron Kovalenko
Employee Title: CEO
Company Phone: 724-318-6672
Company Fax: 866-791-3058
Company Address: PO Box 571 Harmony Ridge, PA 16094
Company Website: www.brightbenchfixers.example
Equipment We Service: Freezers, Cryostorage, Incubators, Centrifuges, Refrigerators, Environmental Chambers, Autoclaves, and more.

Nice to have
• Company Facebook: facebook.com/bbfllc
Company Twitter: @BBFLLC
QR Code (link to website): www.brightbenchfixers.example

```html
<!DOCTYPE html>
<html lang="en">
<head>
<meta charset="utf-8">
<title>Bright Bench Fixers – Business Card</title>
<link rel="stylesheet" href="https://fonts.googleapis.com/css2?family=Open+Sans:wght@400;600;700&display=swap">
<style>
  :root {
    --green: #1fa553;
    --green-dark: #178a44;
    --stripe: rgba(255,255,255,0.06);
    --ink: #1e1e1e;
    --grey: #5a5a5a;
    --paper: #ffffff;
    --backdrop: #e9e7e3;
  }
  * { box-sizing: border-box; margin: 0; padding: 0; }
  html, body { width: 1200px; height: 1023px; overflow: hidden; }
  body {
    background: var(--backdrop);
    font-family: "Open Sans", Arial, sans-serif;
    position: relative;
  }
  .card {
    position: absolute;
    left: 220px;
    width: 760px;
    height: 434px;
    background: var(--paper);
    box-shadow: 0 6px 18px rgba(0,0,0,0.15);
    overflow: hidden;
  }
  .card--front { top: 52px; }
  .card--back { top: 534px; }

  .band {
    position: absolute;
    left: 0; right: 0;
    background-color: var(--green);
    background-image: repeating-linear-gradient(90deg, var(--stripe) 0 6px, transparent 6px 14px);
  }
  .card--front .band--top { top: 0; height: 96px; }
  .card--front .band--bottom { bottom: 0; height: 150px; }
  .card--front .band--top::after,
  .card--front .band--bottom::before {
    content: ""; position: absolute; left: 0; right: 0; height: 6px; background: #d9dcd9;
  }
  .card--front .band--top::after { bottom: 0; }
  .card--front .band--bottom::before { top: 0; }

  .brand {
    position: absolute;
    top: 96px; left: 0; right: 0; height: 188px;
    display: flex; align-items: center; justify-content: center;
  }
  .brand__name {
    font-weight: 600;
    font-size: 96px;
    letter-spacing: 14px;
    color: var(--ink);
  }
  .website--front {
    position: absolute;
    right: 48px; top: 18px;
    font-size: 24px;
    color: #eaf7ee;
    letter-spacing: 0.3px;
  }

  .card--back .band--bottom { bottom: 0; height: 34px; }
  .contact-person {
    position: absolute; left: 48px; top: 52px;
  }
  .contact-person__name {
    font-size: 32px; font-weight: 700; color: var(--green);
  }
  .contact-person__title {
    font-size: 17px; font-weight: 600; color: var(--grey); letter-spacing: 2px; margin-top: 2px;
  }
  .services {
    position: absolute; left: 48px; top: 150px; width: 330px;
  }
  .services__label {
    font-size: 14px; font-weight: 700; color: var(--green);
    letter-spacing: 1.5px; text-transform: uppercase; margin-bottom: 6px;
  }
  .services__list {
    list-style: none; font-size: 14px; line-height: 1.55; color: var(--grey);
    columns: 2; column-gap: 18px;
  }
  .services__list li { break-inside: avoid; }
  .website--back {
    position: absolute; left: 48px; bottom: 66px;
    font-size: 18px; color: var(--grey);
  }
  .back-brand {
    position: absolute; right: 48px; top: 48px;
    font-weight: 600; font-size: 64px; letter-spacing: 10px; color: var(--ink);
  }
  .details {
    position: absolute; right: 48px; top: 170px;
    list-style: none; text-align: right;
    font-size: 18px; color: var(--ink); line-height: 1.5;
  }
  .details li { display: flex; justify-content: flex-end; align-items: center; gap: 10px; }
  .details svg { width: 16px; height: 16px; fill: var(--green); flex: none; }
  .details .address { align-items: flex-start; }
  .details .address svg { margin-top: 6px; }
</style>
</head>
<body>
  <section class="card card--front" aria-label="Card front">
    <div class="band band--top"></div>
    <div class="brand"><span class="brand__name">BBF</span></div>
    <div class="band band--bottom">
      <p class="website website--front">www.brightbenchfixers.example</p>
    </div>
  </section>

  <section class="card card--back" aria-label="Card back">
    <div class="contact-person">
      <p class="contact-person__name">Ron Kovalenko</p>
      <p class="contact-person__title">CEO</p>
    </div>

    <div class="services">
      <p class="services__label">Equipment we service</p>
      <ul class="services__list">
        <li>Freezers</li>
        <li>Cryostorage</li>
        <li>Incubators</li>
        <li>Centrifuges</li>
        <li>Refrigerators</li>
        <li>Environmental Chambers</li>
        <li>Autoclaves</li>
        <li>and more</li>
      </ul>
    </div>

    <p class="website website--back">www.brightbenchfixers.example</p>

    <div class="back-brand">BBF</div>
    <ul class="details">
      <li class="address"><span>PO Box 571 Harmony Ridge,<br>PA 16094</span>
        <svg viewBox="0 0 16 16"><path d="M8 1a5 5 0 0 0-5 5c0 4 5 9 5 9s5-5 5-9a5 5 0 0 0-5-5zm0 7a2 2 0 1 1 0-4 2 2 0 0 1 0 4z"/></svg></li>
      <li><span>724-318-6672</span>
        <svg viewBox="0 0 16 16"><path d="M3.5 1.5l2.5 0 1.2 3-1.6 1.2a8 8 0 0 0 4.7 4.7l1.2-1.6 3 1.2v2.5a1.5 1.5 0 0 1-1.5 1.5A12.5 12.5 0 0 1 2 3a1.5 1.5 0 0 1 1.5-1.5z"/></svg></li>
      <li><span>866-791-3058</span>
        <svg viewBox="0 0 16 16"><path d="M4 1h6l2 2v3H4zM2 7h12a1 1 0 0 1 1 1v5a1 1 0 0 1-1 1H2a1 1 0 0 1-1-1V8a1 1 0 0 1 1-1zm2 3v2h8v-2z"/></svg></li>
    </ul>
    <div class="band band--bottom"></div>
  </section>
</body>
</html>
```